Professional Website Design to match new logo for Medical Legal Company

We have rebranded our company and We want a professional but also dynamic web site design for a group of esteemed doctors that provide expert evaluation of an injured worker in a Workers Compensation case.
​
1. Our target market is both the attorneys who select our doctors and any doctors who would wish to join our group.

2. Notes for the Landing Page:
- We prefer a simpler, sleeker more modern look for the landing page.
- We want a simplified landing page with one image, three buttons highlighted in Content document.
- We want the main image to be black and white but it can be splashed with color.
-We think the landing page might be enhanced by add a dark blue or black as a primary color. Of course please feel free to try any color combination you think might work.
- We want "The Alder Circle" in large letters and "Stewards of a fair and prompt settlement" in small lettering. We don't want icons on the buttons.
- Do not want more than the one picture at top of landing page.
- We do not want any pictures that include faces. Please eliminate or replace. They will not be chosen.
- For the landing page, instead of a second set of photos please experiment with using medical symbols and legal symbols.
​
3. New Company Name: The Alder Circle
New logo is uploaded bronze and grey/silver will be colors although we are still tweaking the colors for more metallic feel. Want simple not busy.

4. The overall Web page design needs to have some website design effect (e,g image rollover, scrolling effect, hover effect etc).

5. Please follow the attached word document file for the page content of the 4 web pages. Do not mix it up.

Previous company website: www.clinjurisreview.example (we wish to convert some of the content from this website to the new brand). Competitor website that we like: www.rxboardly.example

Target Market(s)

Professional Elite. Attorneys and Doctors

Industry/Entity Type

Medical Legal

Coding

Coded - Design and coding required

Number of Pages Required

5+ page

Font styles to use
Other font styles liked:
• Helvetica or maybe font that matches logo. We are open

Colors

Designer to choose colors to be used in the design.

Requirements
Must have
• I can't locate on color scale but we want Bronze and Silver/Grey from logo. Additional colors can be added. Various shades of grey
Nice to have
• Black and white photos, simple elegant design
Should not have
• Images with faces of unknown people

```html
<!DOCTYPE html>
<html lang="en">
<head>
<meta charset="utf-8">
<title>The Alder Circle</title>
<link href="https://fonts.googleapis.com/css2?family=Crimson+Pro:wght@400;500;600&family=Roboto:wght@300;400;500;700&display=swap" rel="stylesheet">
<style>
:root{
  --bronze:#b0744a;
  --bronze-dark:#8f5a35;
  --ink:#2b2b2b;
  --text:#444;
  --muted:#777;
  --line:#dcdcdc;
  --panel:#f2f2f2;
  --bar:#5a5a5a;
  --band:#3c3c3c;
  --white:#fff;
}
*{box-sizing:border-box;margin:0;padding:0}
html,body{width:1200px;height:2732px;overflow:hidden}
body{background:var(--white);font-family:"Roboto",Helvetica,Arial,sans-serif;color:var(--text)}
.serif{font-family:"Crimson Pro",Georgia,serif}

/* header */
.site-header{height:220px;background:var(--panel);text-align:center;padding-top:22px}
.brand{display:inline-flex;align-items:center;gap:12px;font-family:"Crimson Pro",Georgia,serif;font-size:30px;font-weight:600;color:var(--bronze);letter-spacing:1px}
.brand-mark{width:18px;height:18px;background:var(--bronze)}
.site-header h1{font-family:"Crimson Pro",Georgia,serif;font-weight:500;font-size:46px;color:var(--ink);margin-top:24px}
.site-header .tagline{font-size:17px;color:var(--muted);margin-top:6px}

.hero{height:392px;background:linear-gradient(120deg,#6e6e6e 0%,#bdbdbd 35%,#e4e4e4 55%,#9a9a9a 80%,#5c5c5c 100%)}

/* welcome */
.welcome{display:flex;padding:72px 40px 0 40px;height:740px - 0}
.welcome{height:300px}
.welcome h2{width:560px;font-family:"Crimson Pro",Georgia,serif;font-weight:400;font-size:36px;line-height:1.3;color:var(--ink)}
.mandate{margin-left:120px;width:440px}
.mandate-item{display:flex;gap:18px;font-size:17px;color:var(--text);margin-bottom:14px}
.mandate-item span{color:var(--muted);font-size:20px;width:28px}
.btn{display:inline-block;margin-top:40px;background:var(--bronze);color:var(--white);font-size:15px;padding:14px 40px;text-decoration:none}

/* partnership */
.partnership{padding:0 40px;height:460px}
.partnership h2{font-family:"Crimson Pro",Georgia,serif;font-weight:400;font-size:34px;color:var(--ink);margin-bottom:18px}
.duty-table{display:flex;gap:20px}
.duty-col .bar{background:var(--bar);color:var(--white);text-align:center;font-family:"Crimson Pro",Georgia,serif;font-size:20px;padding:10px 0}
.duty-main{width:860px}
.duty-member{width:240px}
.duty-lists{display:flex;padding:20px 0 0 20px;gap:40px}
.duty-lists ul{list-style:none;width:270px}
.duty-lists li{font-size:13px;color:var(--text);padding:8px 0;border-bottom:1px solid #eee}
.duty-lists li::before{content:"– ";color:var(--bronze)}

/* band */
.value-band{height:340px;background:var(--band);color:var(--white);text-align:center;padding-top:62px}
.value-band h2{font-family:"Crimson Pro",Georgia,serif;font-weight:400;font-size:34px;line-height:1.3;width:900px;margin:0 auto}
.value-band .small{font-size:13px;color:#cfcfcf;margin-top:22px}
.value-band .strong{font-size:15px;font-weight:500;margin-top:12px}

/* expectations */
.expect{padding:90px 90px 0;height:600px}
.expect h2{font-family:"Crimson Pro",Georgia,serif;font-weight:400;font-size:36px;line-height:1.3;text-align:center;color:var(--ink);margin-bottom:54px}
.expect-grid{display:grid;grid-template-columns:1fr 1fr;column-gap:70px;row-gap:30px}
.expect-item{display:flex;gap:18px;align-items:flex-start;font-size:13px;line-height:1.45;color:var(--text)}
.expect-item b{color:var(--ink);font-weight:700}
.expect-item svg{flex:none}

/* footer */
.site-footer{height:372px;background:var(--panel);padding:40px 40px 0;position:relative}
.footer-cols{display:flex}
.footer-contact{width:780px;font-size:13px;line-height:1.7;color:var(--text)}
.footer-contact .label{margin-top:26px;font-weight:500;color:var(--ink)}
.footer-links{width:190px;font-size:13px;line-height:2;color:var(--text)}
.copyright{position:absolute;left:40px;bottom:30px;font-size:12px;color:var(--muted)}
</style>
</head>
<body>

<header class="site-header">
  <div class="brand"><span class="brand-mark"></span>THE ALDER CIRCLE</div>
  <h1>Guardians of your Reputation</h1>
  <p class="tagline">Guardians of your most valuable asset, your time</p>
</header>

<div class="hero" role="img" aria-label="Black and white photo of a hand writing on a clipboard with a pen"></div>

<section class="welcome">
  <h2>Welcome to The Alder Circle, where our philosophy centers on a dual mandate,</h2>
  <div class="mandate">
    <div class="mandate-item"><span>01</span>To support our Physicians in achieving the pinnacle of medical legal reporting</div>
    <div class="mandate-item"><span>02</span>Maximizing Physician time spent</div>
    <a class="btn" href="#">Connect with a Physician Advisor</a>
  </div>
</section>

<section class="partnership">
  <h2>Partnership With Shared Duties</h2>
  <div class="duty-table">
    <div class="duty-col duty-main">
      <div class="bar">Alder Circle</div>
      <div class="duty-lists">
        <ul>
          <li>Schedule Appointment</li>
          <li>Mail Confirmation</li>
          <li>Book and Pay Room</li>
          <li>Schedule Interpreter</li>
          <li>Obtain Thorough Patient History Online</li>
          <li>Obtain Records/Cover Letter</li>
          <li>Prepare Export of Records</li>
          <li>Transcribe Report</li>
        </ul>
        <ul>
          <li>Comprehensive Edit</li>
          <li>Bill Report</li>
          <li>Collect</li>
          <li>Panel Data Analysis (Locations)</li>
          <li>Physician Marketing</li>
          <li>Location Management (over 300 locations)</li>
          <li>DWC Logistics</li>
        </ul>
      </div>
    </div>
    <div class="duty-col duty-member">
      <div class="bar">Member QME</div>
      <div class="duty-lists">
        <ul>
          <li>Conduct Exam</li>
          <li>Submit Exam Notes and Findings</li>
          <li>Review and Approve Final Report</li>
        </ul>
      </div>
    </div>
  </div>
</section>

<section class="value-band">
  <h2>The Alder Circle looks to attract Physicians that share our commitment to a High Standard in both Timeliness and Comprehensive Evidenced Based Medical Reporting.</h2>
  <p class="small">Following is our Value Statement to our targeted legal community:</p>
  <p class="strong">The Alder Circle strives to uphold the Highest Standard in Medical Reporting.</p>
</section>

<section class="expect">
  <h2>Following is a list to best describe what to expect when you<br>receive QME Report from one of our Guardians:</h2>
  <div class="expect-grid">
    <div class="expect-item"><svg width="30" height="30" viewBox="0 0 30 30"><circle cx="15" cy="15" r="12" fill="none" stroke="#555" stroke-width="1.5"/><path d="M15 8v7l5 3" fill="none" stroke="#555" stroke-width="1.5"/></svg><p><b>Timely:</b> Unless special circumstances exist, you can expect to receive the report well ahead of DWC imposed deadlines</p></div>
    <div class="expect-item"><svg width="30" height="30" viewBox="0 0 30 30"><rect x="6" y="4" width="18" height="22" fill="none" stroke="#555" stroke-width="1.5"/><path d="M10 11h10M10 15h10M10 19h6" stroke="#555" stroke-width="1.5"/></svg><p><b>Detailed and Comprehensive</b> Medical History</p></div>
    <div class="expect-item"><svg width="30" height="30" viewBox="0 0 30 30"><rect x="4" y="7" width="22" height="16" fill="none" stroke="#555" stroke-width="1.5"/><path d="M8 12h14M8 17h9" stroke="#555" stroke-width="1.5"/></svg><p><b>Clear, Concise and Readable:</b> So your valuable time is not wasted</p></div>
    <div class="expect-item"><svg width="30" height="30" viewBox="0 0 30 30"><circle cx="13" cy="13" r="8" fill="none" stroke="#555" stroke-width="1.5"/><path d="M19 19l7 7" stroke="#555" stroke-width="1.5"/></svg><p><b>Comprehensive Analysis</b> of all injured body parts focused on the medical legal aspects of the case</p></div>
    <div class="expect-item"><svg width="30" height="30" viewBox="0 0 30 30"><circle cx="15" cy="15" r="12" fill="none" stroke="#555" stroke-width="1.5"/><path d="M9 15l4 4 8-8" fill="none" stroke="#555" stroke-width="1.5"/></svg><p><b>No Conclusory Findings:</b> Thoroughly discussed conclusions for Apportionment, Causation and Impairment that are medical evidence based</p></div>
    <div class="expect-item"><svg width="30" height="30" viewBox="0 0 30 30"><circle cx="15" cy="15" r="12" fill="none" stroke="#555" stroke-width="1.5"/><path d="M11 12a4 4 0 1 1 5 4v3M15 22v1" fill="none" stroke="#555" stroke-width="1.5"/></svg><p><b>Answers</b> to all questions stated in the Cover Letter</p></div>
    <div class="expect-item"><svg width="30" height="30" viewBox="0 0 30 30"><path d="M15 4v22M6 10h18M6 10l-3 8h6zM24 10l-3 8h6z" fill="none" stroke="#555" stroke-width="1.5"/></svg><p><b>Impartial:</b> (all of our reports are reviewed by a 3rd party for Objectivity)</p></div>
    <div class="expect-item"><svg width="30" height="30" viewBox="0 0 30 30"><path d="M15 25s-10-6-10-13a5 5 0 0 1 10-2 5 5 0 0 1 10 2c0 7-10 13-10 13z" fill="none" stroke="#555" stroke-width="1.5"/></svg><p><b>Future Medical Care</b> Section that is thoughtful and addresses both the short term and long term needs of the applicant</p></div>
    <div class="expect-item"><svg width="30" height="30" viewBox="0 0 30 30"><path d="M6 22l6-6 5 4 8-10" fill="none" stroke="#555" stroke-width="1.5"/></svg><p><b>High Level Review</b> of Records by the Physician with Commentary</p></div>
  </div>
</section>

<footer class="site-footer">
  <div class="footer-cols">
    <div class="footer-contact">
      <div class="brand" style="font-size:24px"><span class="brand-mark" style="width:14px;height:14px"></span>THE ALDER CIRCLE</div>
      <p class="label">Headquarters</p>
      <p>2280 Marlow Avenue<br>3rd Floor<br>Westbrook, CA 90412</p>
      <p class="label" style="margin-top:16px">Call toll free (555) 014-2290</p>
      <p><b style="color:var(--ink);font-weight:500">Fax</b> (555) 014-2291</p>
    </div>
    <div class="footer-links" style="padding-top:56px">Continuing Education Courses<br>QME Test Resources<br>Newsletter</div>
    <div class="footer-links" style="padding-top:56px">Upcoming Events<br>Current Member Login</div>
  </div>
  <p class="copyright">© 2022 Clinjuris Review</p>
</footer>

</body>
</html>
```